Valdoria necesita diseños de papeleria como tarjeta de presentacion, hoja membretada, sobres...

La papelería corporativa es para una tienda de moda multimarcas ubicada en Ecuador.
Los diseños tienen que ser de acuerdo a los diseños que adjunto.

```html
<!DOCTYPE html>
<html lang="es">
<head>
<meta charset="utf-8">
<title>Valdoria – Hoja membretada</title>
<link href="https://fonts.googleapis.com/css2?family=Lato:ital,wght@0,400;0,700;1,400;1,700&display=swap" rel="stylesheet">
<style>
  :root {
    --backdrop: #cbbfbe;
    --paper: #ffffff;
    --ink: #3a3a3c;
    --ink-soft: #5a5a5c;
    --rule: #8a8a8a;
    --accent: #e3261c;
  }
  * { margin: 0; padding: 0; box-sizing: border-box; }
  html, body {
    width: 1200px; height: 784px; overflow: hidden;
    background: var(--backdrop);
    font-family: "Lato", sans-serif;
  }
  .letterhead {
    position: absolute;
    left: 333px; top: 22px;
    width: 534px; height: 740px;
    background: var(--paper);
    box-shadow: 0 2px 10px rgba(0,0,0,0.12);
    color: var(--ink);
  }
  .brand {
    position: absolute;
    right: 44px; top: 46px;
    text-align: left;
  }
  .brand-name {
    font-weight: 700;
    font-size: 38px;
    letter-spacing: 8px;
    color: var(--ink);
    line-height: 1;
  }
  .brand-tagline {
    font-size: 11px;
    letter-spacing: 6.2px;
    color: var(--ink-soft);
    margin-top: 6px;
  }
  .letter {
    position: absolute;
    left: 52px; top: 150px;
    width: 420px;
    font-style: italic;
    font-size: 9.6px;
    line-height: 1.45;
  }
  .letter p { margin-bottom: 12px; }
  .letter .indent { padding-left: 18px; }
  .salutation { margin-bottom: 10px; }
  .signoff { margin-top: 4px; line-height: 1.5; }
  .signoff strong { font-weight: 700; }
  .footer {
    position: absolute;
    left: 40px; right: 40px; bottom: 40px;
  }
  .footer-title {
    display: flex; align-items: center; gap: 10px;
    font-size: 10.5px; color: var(--accent);
    white-space: nowrap;
  }
  .footer-title::before, .footer-title::after {
    content: ""; flex: 1; height: 1px; background: var(--rule);
  }
  .footer-contact {
    text-align: center;
    font-size: 9.6px; font-style: italic;
    margin-top: 10px;
  }
</style>
</head>
<body>
  <main class="letterhead">
    <header class="brand">
      <div class="brand-name">VALDORIA</div>
      <div class="brand-tagline">MODA &amp; LENCERIA</div>
    </header>

    <section class="letter">
      <p class="salutation">Dear Sir/Mam,</p>
      <p class="indent">Contrary to popular belief, Lorem Ipsum is not simply random text. It has roots in a piece of classical Latin literature from 45 BC, making it over 2000 years old. Tomas Ferrer, a Latin professor at Brightwater College in Virginia, looked up one of the more obscure Latin words, consectetur, from a Lorem Ipsum passage, and going through the cites of the word in classical literature, discovered the undoubtable source.</p>
      <p class="indent">Lorem Ipsum comes from sections 1.10.32 and 1.10.33 of "de Finibus Bonorum et Malorum" (The Extremes of Good and Evil) by Lucius Varro, written in 45 BC. This book is a treatise on the theory of ethics, very popular during the Renaissance. The first line of Lorem Ipsum, "Lorem ipsum dolor sit amet..", comes from a line in section 1.10.32.</p>
      <p class="indent">The standard chunk of Lorem Ipsum used since the 1500s is reproduced below for those interested. Sections 1.10.32 and 1.10.33 from "de Finibus Bonorum et Malorum" by Lucius Varro are also reproduced in their exact original form, accompanied by English versions from the 1914 translation by J. Whitlow.</p>
      <p class="indent">The standard chunk of Lorem Ipsum used since the 1500s is reproduced below for those interested.</p>
      <div class="signoff">
        <strong>Best Regards</strong><br>
        <strong>Lena Ortiz</strong><br>
        Valdoria Moda &amp; Lencria Inc
      </div>
    </section>

    <footer class="footer">
      <div class="footer-title">VALDORIA MODA &amp; LENCRIA INC</div>
      <div class="footer-contact">1234567890 / info@yourmail.com / www.yourwebsite.com / P.O. Box 5555 Your City Address Here</div>
    </footer>
  </main>
</body>
</html>
```